依頼詳細
利用先は3パターンとなり、それぞれでデザインを作成して頂きます。
<利用先>
・ポスティング(A4)
・事務所壁に設置するポスター(B0サイズ)
・車両に貼付けするマグネットシート(縦横30cm幅でバンの後ろに取付)※左右2枚に分けてか1枚に収まるでも可
記載項目
社名、求人条件https://jp.shigotomadoguchi.net/q-%E9%9B%BB%E6%B0%97%E5%B7%A5%E4%BA%8B%E5%A3%AB-l-%E5%85%B5%E5%BA%AB%E7%9C%8C-%E5%8A%A0%E5%8F%A4%E5%B7%9D%E5%B8%82-%E6%B1%82%E4%BA%BA.html?vjk=3f91c2b7d05e6a48&advn=2739481650274813

別途添付資料の分析表
サイズ
ポスティングA4、ポスターB0、マグネットシート縦横30cm
ページ数
片面
希望イメージ
シンプル 複雑
単色 カラフル
暗い 明るい
日常 高級
遊び心 厳粛
未来的 伝統的
女性的 男性的
希望する色
緑系、水色系
納品ファイル
• イラストレーター形式 (.ai)
補足説明

メッセージではご連絡させていただいておりましたが、非常にわかりやすいデザインで目が惹かれました。
よろしくお願いいたします。

この度はご提案いただき誠にありがとうございました。
皆さん非常に目の惹かれるデザインでしたが、社内にて検討の結果選定させていただきました。

また、今後依頼させていただくことも増える予定ですので機会がございましたらその際はよろしくお願いいたします。

```html
<!DOCTYPE html>
<html lang="ja">
<head>
<meta charset="utf-8">
<title>電気工事士 募集</title>
<link rel="stylesheet" href="https://fonts.googleapis.com/css2?family=Noto+Sans+JP:wght@500;700;900&family=Noto+Serif+JP:wght@700;900&display=swap">
<style>
:root{
  --blue:#1f3f9c;
  --shadow:#9aa6c4;
  --ink:#1a1a1a;
  --band-top:#f2f2f2;
  --band-bottom:#c9c9c9;
  --green-light:#c9ea8a;
  --green:#7cc242;
  --green-deep:#4f9a22;
  --paper:#ffffff;
}
*{margin:0;padding:0;box-sizing:border-box}
html,body{width:1200px;height:1200px;overflow:hidden;background:var(--paper)}
.poster{position:relative;width:1200px;height:1200px;background:var(--paper);font-family:"Noto Sans JP",sans-serif;color:var(--ink)}
.title{position:absolute;left:0;top:0;width:1200px;text-align:center;font-weight:900;font-size:210px;line-height:240px;letter-spacing:24px;padding-left:24px;color:var(--blue);
  text-shadow:6px 6px 0 var(--shadow)}
.company{position:absolute;left:36px;top:284px;width:410px;height:120px}
.company .mark{position:absolute;left:0;top:14px;width:72px;height:72px;border-radius:50%;background:var(--green)}
.company .tagline{position:absolute;left:88px;top:10px;white-space:nowrap;font-weight:700;font-size:25px;line-height:30px}
.company .name{position:absolute;left:86px;top:38px;font-family:"Noto Serif JP",serif;font-weight:900;font-size:64px;line-height:72px;letter-spacing:2px}
.phone{position:absolute;left:36px;top:404px;display:flex;align-items:center;gap:8px;font-weight:700;font-size:46px;line-height:58px;white-space:nowrap}
.phone svg{width:38px;height:38px}
.address{position:absolute;left:140px;top:476px;font-family:"Noto Serif JP",serif;font-weight:700;font-size:30px;line-height:36px;white-space:nowrap}
.recruit{position:absolute;left:461px;top:271px;width:708px;height:310px;border:8px solid var(--blue);display:flex}
.recruit span{flex:1;display:flex;align-items:center;justify-content:center;font-weight:900;font-size:265px;line-height:1}
.recruit .left{background:var(--blue);color:var(--paper)}
.recruit .right{background:var(--paper);color:var(--blue)}
.band{position:absolute;left:36px;width:1140px;height:34px;background:linear-gradient(var(--band-top),var(--band-bottom));color:var(--blue);font-weight:900;font-size:28px;line-height:34px;padding-left:10px}
.list{position:absolute;left:40px;font-weight:700;white-space:nowrap}
.pay{top:638px;font-size:33px;line-height:43px}
.pay .indent{padding-left:30px}
.welfare{top:898px;font-size:30px;line-height:37px}
.apply{top:1088px;font-size:30px;line-height:42px}
.bubble{position:absolute;z-index:2;left:876px;top:680px;width:252px;height:252px;border-radius:50%;
  background:radial-gradient(circle at 40% 30%,var(--green-light),var(--green) 55%,var(--green-deep));
  display:flex;align-items:center;justify-content:center;text-align:center;color:var(--paper);font-weight:700;font-size:34px;line-height:52px}
</style>
</head>
<body>
<main class="poster">
  <h1 class="title">電気工事士</h1>

  <div class="company">
    <span class="mark"></span>
    <p class="tagline">太陽光発電施工　株式会社</p>
    <p class="name">SOLVA</p>
  </div>

  <p class="phone">
    <svg viewBox="0 0 24 24" aria-hidden="true"><path fill="#1a1a1a" d="M6.6 10.8a15.1 15.1 0 0 0 6.6 6.6l2.2-2.2a1 1 0 0 1 1-.25 11.4 11.4 0 0 0 3.6.57 1 1 0 0 1 1 1V20a1 1 0 0 1-1 1A17 17 0 0 1 3 4a1 1 0 0 1 1-1h3.5a1 1 0 0 1 1 1c0 1.25.2 2.45.57 3.57a1 1 0 0 1-.25 1z"/></svg>
    079-000-5821
  </p>
  <p class="address">兵庫県青葉市<br>緑ヶ丘町北二丁目45</p>

  <div class="recruit"><span class="left">募</span><span class="right">集</span></div>

  <h2 class="band" style="top:595px">雇用形態 ：正社員</h2>
  <div class="list pay">
    <p>月給：280,000円～400,000円（経験年数5年以上）</p>
    <p class="indent">（※想定年収 4,000,000円～5,600,000円）</p>
    <p class="indent">・500,000円～637,000円（経験年数10年以上）</p>
    <p class="indent">（※想定年収 5,000,000円～8,918,000円）</p>
    <p class="indent">・経験・能力に応じて変動有り</p>
  </div>

  <div class="bubble">お気軽に<br>お問い合わせ<br>下さい</div>

  <h2 class="band" style="top:857px">福利厚生</h2>
  <div class="list welfare">
    <p>□昇給年2回　□雇用保険　□厚生年金　□健康保険</p>
    <p>□労災保険　□交通費支給あり（マイカー通勤可、無料駐車場有）</p>
    <p>□資格取得支援・手当てあり　□制服貸与</p>
    <p>□有給休暇（6か月経過後10日付与※最大20日付与）</p>
  </div>

  <h2 class="band" style="top:1051px">応募条件</h2>
  <div class="list apply">
    <p>・電気工事経験5年以上</p>
    <p>・第一種電気工事士または第二種電気工事士の資格保有者</p>
  </div>
</main>
</body>
</html>
```